Hollow-Lanterns charity auctions

We need a three part design for a nonprofit charity auction platform. This platform will eventually interface with a cell phone app, therefore the initial design needs to be responsive. Each phase should produce a working web page that builds upon the previous phase. The first phase is strictly to be a content page which can present our YouTube channel. It should also be a direct link between our alternate social media resources, e.g. FB, Chirper, Snapgram etc. We can afford $500 for each phase (total $1500). Only serious long-term designers need respond.

Target Market(s)

High profile celebrities
International Bidders
Social Media

Industry/Entity Type

Cell Phone

Number of Pages Required

5+ page

Requirements
Must have
• Logos
• Responsive between desktop and cell phone website
• Upgradeable
• Hyper text
• Blog
• Flash (with video and image storage) i.e. YouTube, Snapgram, Pinterest etc.
• Background music
Nice to have
• Intuitive with action buttons e.g. automatic post buttons, play buttons, stop buttons etc

```html
<!DOCTYPE html>
<html lang="en">
<head>
<meta charset="utf-8">
<title>Hollow Lanterns</title>
<link href="https://fonts.googleapis.com/css2?family=Open+Sans:wght@400;600;700&display=swap" rel="stylesheet">
<style>
:root{
  --black:#000;
  --ink:#2b2b2b;
  --body:#777;
  --gold:#f0a91e;
  --gold-light:#f5b833;
  --gold-dark:#e49a10;
  --white:#fff;
  --rule:#e2e2e2;
  --search:#2a2a2a;
}
*{margin:0;padding:0;box-sizing:border-box}
html,body{width:804px;height:1200px;overflow:hidden;background:var(--white)}
body{position:relative;font-family:"Open Sans",Arial,sans-serif;color:var(--ink)}
.abs{position:absolute}

.site-header{left:0;top:0;width:804px;height:125px;background:var(--black)}
.brand{left:98px;top:20px;display:flex;align-items:center;gap:10px}
.brand-mark{width:48px;height:48px;border-radius:50%;background:var(--gold)}
.brand-name{color:var(--white);font-weight:400;font-size:12px;letter-spacing:5px;line-height:14px;text-transform:uppercase}
.music-btn{left:478px;top:31px;width:28px;height:28px;border-radius:50%;background:var(--gold)}
.search{left:521px;top:31px;width:189px;height:27px;background:var(--search);color:#888;font-size:9px;padding:7px 14px}
.search svg{position:absolute;right:12px;top:6px}

.main-nav{left:94px;top:87px;width:616px;height:38px;background:linear-gradient(var(--gold-light),var(--gold-dark));border-radius:5px 5px 0 0}
.main-nav a{position:absolute;top:13px;transform:translateX(-50%);color:var(--white);font-size:9.5px;font-weight:700;text-decoration:none;white-space:nowrap}
.main-nav i{position:absolute;top:0;width:1px;height:38px;background:rgba(0,0,0,.08)}

.hero{left:0;top:125px;width:804px;height:356px;background:linear-gradient(100deg,#5d5443 0%,#b9b7b0 30%,#d9d6cf 55%,#a7a39a 80%,#4a3f36 100%)}
.hero-caption{left:94px;top:231px;width:331px;height:114px;background:rgba(40,40,40,.55);padding:14px 22px}
.hero-caption h1{color:var(--gold);font-size:25px;font-weight:700;letter-spacing:-.5px;line-height:30px;text-transform:uppercase}
.hero-caption p{color:var(--white);font-size:8.6px;line-height:15px;margin-top:8px}
.hero-arrow{top:272px}
.hero-shadow{left:0;top:480px;width:804px;height:24px;background:radial-gradient(ellipse at top,rgba(0,0,0,.18),transparent 70%)}

.section-title{left:94px;font-size:16px;font-weight:700;color:var(--ink);text-transform:uppercase}
.section-title span{color:var(--gold)}
.rule{left:94px;width:616px;height:2px;background:var(--rule)}

.video{left:94px;top:553px;width:185px;height:122px;background:radial-gradient(circle at 45% 55%,#d8c9a3,#6b5a3a 45%,#1d1a14 85%)}
.video-bar{left:0;bottom:0;width:100%;height:14px;background:#111}
.video-top{left:0;top:0;width:100%;height:13px;background:rgba(0,0,0,.7);color:var(--white);font-size:5.5px;text-align:right;padding:3px 6px}
.play{left:78px;top:46px;width:30px;height:30px;background:#a3151a;border-radius:4px}
.intro{left:303px;top:553px;width:407px;font-size:8px;line-height:15.3px;color:var(--body);text-align:justify}
.btn{left:301px;top:650px;width:69px;height:26px;border-radius:13px;background:linear-gradient(var(--gold-light),var(--gold-dark));color:var(--white);font-size:8.5px;text-align:center;line-height:26px}

.card{top:741px;width:184px}
.card-img{width:184px;height:102px}
.card-meta{position:relative;height:20px;margin-top:13px}
.pill{position:absolute;top:0;height:20px;border:1px solid #ddd;border-radius:2px;font-size:7px;color:var(--body);line-height:18px;padding:0 9px}
.pill.count{right:0;width:34px;color:var(--ink);font-weight:700;text-align:right}
.pill.count svg{position:absolute;left:7px;top:5px}
.card p{margin-top:9px;font-size:8px;line-height:14px;color:var(--body);text-align:justify}
.card-shadow{top:843px;width:220px;height:14px;background:radial-gradient(ellipse at top,rgba(0,0,0,.12),transparent 70%)}

.site-footer{left:0;top:959px;width:804px;height:195px;background:linear-gradient(var(--gold-light),var(--gold-dark))}
.foot-col{top:22px;width:130px}
.foot-col h3{color:var(--white);font-size:11.5px;font-weight:600;text-transform:uppercase;padding-bottom:9px;border-bottom:1px solid rgba(255,255,255,.25)}
.foot-col ul{list-style:none;margin-top:11px}
.foot-col li{color:var(--white);font-size:7px;line-height:17.6px;text-transform:uppercase}
.social{position:absolute;left:0;width:34px;height:34px;border:2px solid var(--white)}
.social-label{position:absolute;left:51px;color:var(--white);font-size:8.5px;text-transform:uppercase}
.bottom-bar{left:0;top:1154px;width:804px;height:46px;background:var(--black);color:#ccc;font-size:8px;text-align:center;line-height:46px}
</style>
</head>
<body>

<header class="site-header abs">
  <div class="brand abs">
    <div class="brand-mark"></div>
    <div class="brand-name">Hollow<br>Lanterns</div>
  </div>
  <div class="music-btn abs">
    <svg width="28" height="28" viewBox="0 0 28 28"><path d="M11 19V9l9-2v10" fill="none" stroke="#000" stroke-width="2"/><circle cx="9" cy="19" r="2.6"/><circle cx="18" cy="17" r="2.6"/></svg>
  </div>
  <div class="search abs">Search
    <svg width="15" height="15" viewBox="0 0 15 15"><circle cx="6" cy="6" r="4.5" fill="none" stroke="#888" stroke-width="1.5"/><path d="M9.5 9.5 14 14" stroke="#888" stroke-width="1.8"/></svg>
  </div>
</header>

<nav class="main-nav abs">
  <a style="left:45px">HOME</a><i style="left:86px"></i>
  <a style="left:133px">ABOUT US</a><i style="left:180px"></i>
  <a style="left:226px">SERVICES</a><i style="left:272px"></i>
  <a style="left:310px">BLOG</a><i style="left:345px"></i>
  <a style="left:386px">VIDEO</a><i style="left:424px"></i>
  <a style="left:463px">NEWS</a><i style="left:500px"></i>
  <a style="left:555px">CONTACT US</a>
</nav>

<section class="hero abs" role="img" aria-label="Bright living room with framed forest paintings, sofa with cushions, glass table and wooden chests">
</section>
<div class="hero-caption abs">
  <h1>Hollow Lanterns</h1>
  <p>Lorem ipsum dolor sit amet, consectetuer adipiscing elit. Aenean commodo ligula eget dolor. Aenean massa. Cum sociis natoque penatibus et magnis dis parturient montes, nascetur ridiculus mus.</p>
</div>
<svg class="hero-arrow abs" style="left:20px" width="18" height="32" viewBox="0 0 18 32"><path d="M16 2 2 16l14 14" fill="none" stroke="#fff" stroke-width="2"/></svg>
<svg class="hero-arrow abs" style="left:760px" width="18" height="32" viewBox="0 0 18 32"><path d="M2 2l14 14L2 30" fill="none" stroke="#fff" stroke-width="2"/></svg>
<div class="hero-shadow abs"></div>

<h2 class="section-title abs" style="top:503px">Welcome to <span>Town of Bramblewick</span></h2>
<div class="rule abs" style="top:531px"></div>

<div class="video abs" role="img" aria-label="Video still of diamond rings on a sparkling background">
  <div class="video-top abs">Share &nbsp; More info</div>
  <div class="play abs"><svg width="30" height="30" viewBox="0 0 30 30"><path d="M11 8v14l11-7z" fill="#fff"/></svg></div>
  <div class="video-bar abs"></div>
</div>
<p class="intro abs">Lorem ipsum dolor sit amet, consectetuer adipiscing elit. Aenean commodo ligula eget dolor. Aenean massa. Cum sociis natoque penatibus et magnis dis parturient montes, nascetur ridiculus mus. Donec quam felis, ultricies nec, pellentesque eu, pretium quis, sem. Nulla consequat massa quis enim. Donec pede justo, fringilla vel, aliquet nec, vulputate eget, arcu. In enim justo, rhoncus ut, imperdiet a, venenatis vitae, justo.Nullam dictum felis eu pede mollis pretium. Integer tincidunt. Cras dapibus. Vivamus elementum semper nisi. Aenean vulputate eleifend tellus. Aenean leo ligula, porttitor eu, consequat vitae,</p>
<div class="btn abs">Read More</div>

<h2 class="section-title abs" style="top:696px">Latest <span>Blog</span></h2>
<div class="rule abs" style="top:725px"></div>

<div class="card-shadow abs" style="left:76px"></div>
<div class="card-shadow abs" style="left:294px"></div>
<div class="card-shadow abs" style="left:508px"></div>

<article class="card abs" style="left:94px">
  <div class="card-img" role="img" aria-label="Bright kitchen with a round dining table and chairs" style="background:linear-gradient(#f1ece4,#c9b39a 60%,#7a5a3e)"></div>
  <div class="card-meta"><span class="pill">JANUARY 14 , 2015</span><span class="pill count"><svg width="12" height="9" viewBox="0 0 12 9"><ellipse cx="6" cy="4" rx="6" ry="4"/></svg>2</span></div>
  <p>Companies have a variety of needs and potential problems. Recognizing your risks and taking measures to protect your</p>
</article>
<article class="card abs" style="left:312px">
  <div class="card-img" role="img" aria-label="Pearl necklace draped over an ornate antique box" style="background:linear-gradient(120deg,#e8e1d6,#a8957a 50%,#3e3225)"></div>
  <div class="card-meta"><span class="pill">JANUARY 14 , 2015</span><span class="pill count"><svg width="12" height="9" viewBox="0 0 12 9"><ellipse cx="6" cy="4" rx="6" ry="4"/></svg>2</span></div>
  <p>Companies have a variety of needs and potential problems. Recognizing your risks and taking measures to protect your</p>
</article>
<article class="card abs" style="left:526px">
  <div class="card-img" role="img" aria-label="Light bedroom with a white bed, desk and windows" style="background:linear-gradient(#eef0ef,#d8d2cc 55%,#9c5a5e)"></div>
  <div class="card-meta"><span class="pill">JANUARY 14 , 2015</span><span class="pill count"><svg width="12" height="9" viewBox="0 0 12 9"><ellipse cx="6" cy="4" rx="6" ry="4"/></svg>2</span></div>
  <p>Companies have a variety of needs and potential problems. Recognizing your risks and taking measures to protect your</p>
</article>

<footer class="site-footer abs">
  <div class="foot-col abs" style="left:95px"><h3>Navigation</h3><ul><li>Home</li><li>About us</li><li>Blog</li><li>Contact us</li><li>Company sign up</li><li>Login</li><li>Terms and conditions</li></ul></div>
  <div class="foot-col abs" style="left:258px"><h3>Hollow Lanterns</h3><ul><li>Home</li><li>About us</li><li>Blog</li><li>Contact us</li><li>Company sign up</li><li>Login</li><li>Terms and conditions</li></ul></div>
  <div class="foot-col abs" style="left:424px"><h3>Category</h3><ul><li>Home</li><li>About us</li><li>Blog</li><li>Contact us</li><li>Company sign up</li><li>Login</li><li>Terms and conditions</li></ul></div>
  <div class="foot-col abs" style="left:588px;width:130px"><h3>Follow us</h3>
    <div class="social" style="top:40px"></div><span class="social-label" style="top:52px">Friendpage</span>
    <div class="social" style="top:81px"></div><span class="social-label" style="top:93px">Chirper</span>
    <div class="social" style="top:121px"></div><span class="social-label" style="top:134px">Snapgram</span>
  </div>
</footer>
<div class="bottom-bar abs">Copyright ©2014 &nbsp;Hollow Lanterns &nbsp;| &nbsp;All rights reserved</div>

</body>
</html>
```